Optometry practice sign/banner

Modern design appeal to mix demographic, family friendly. Emphasize the importance of eye exam.
Brigh colors, green,blue, yellow,
Photo of people wearing glasses
4'x8'

" EYE EXAM, CONTACT LENS, ORTHOK, LASIK CONSULTATION, DIABETES RETINAL EXAM
DR. NORA PEL
TALVIN OPTOMETRY " Eyecare for your family"
555.762.4139
MEDICAL, VITALBASE, QRT, BRAVELINK, WALK IN WELCOME"

Target Market(s)

Family, middle age, mix demographic

Colors
33b8a4
fbee3d
cee9f5
9bcb3c

Requirements
Nice to have
• Photo of family wearing glasses.

```html
<!DOCTYPE html>
<html lang="en">
<head>
<meta charset="UTF-8">
<title>Talvin Optometry Banner</title>
<link href="https://fonts.googleapis.com/css2?family=Arimo:wght@400;700&display=swap" rel="stylesheet">
<style>
  :root {
    --teal: #1bb39c;
    --green: #8cc63f;
    --green-text: #9bcb3c;
    --yellow: #fbe625;
    --ink: #1f1f1f;
    --brand-ink: #3a3330;
    --white: #ffffff;
    --bg-top: #bdb1ab;
    --bg-mid: #a89a95;
    --bg-bottom: #8a7b78;
    --page: #eef1f4;
  }
  * { margin: 0; padding: 0; box-sizing: border-box; }
  html, body {
    width: 1200px; height: 800px; overflow: hidden;
    background: var(--page);
    font-family: "Arimo", Arial, sans-serif;
  }
  .banner {
    position: absolute; left: 0; top: 120px;
    width: 1200px; height: 560px; overflow: hidden;
    background: linear-gradient(180deg, var(--bg-top) 0%, var(--bg-mid) 55%, var(--bg-bottom) 100%);
  }
  .family-photo {
    position: absolute; left: 0; top: 0; width: 700px; height: 560px;
    background:
      radial-gradient(ellipse 200px 230px at 260px 260px, #e4b9a4 0%, rgba(228,185,164,0) 100%),
      radial-gradient(ellipse 170px 200px at 470px 190px, #efc9b3 0%, rgba(239,201,179,0) 100%),
      radial-gradient(ellipse 260px 240px at 460px 100px, #9a5234 0%, rgba(154,82,52,0) 100%),
      radial-gradient(ellipse 240px 200px at 460px 480px, #f2c9d3 0%, rgba(242,201,211,0) 100%),
      linear-gradient(90deg, #6a3a28 0%, #a86a50 35%, rgba(180,160,150,0.4) 80%, rgba(180,160,150,0) 100%);
  }
  .phone {
    position: absolute; left: 640px; top: 23px;
    display: flex; align-items: center; gap: 14px;
    font-weight: 700; font-size: 40px; line-height: 40px; color: var(--ink);
  }
  .phone-icon { width: 36px; height: 36px; }
  .brand {
    position: absolute; left: 985px; top: 20px; width: 140px;
    display: flex; flex-direction: column; align-items: center; gap: 14px;
  }
  .brand-square { width: 100px; height: 100px; background: var(--yellow); }
  .brand-name {
    font-weight: 400; font-size: 20px; line-height: 20px; color: var(--brand-ink);
    letter-spacing: 1px; text-align: center;
  }
  .services {
    position: absolute; left: 745px; top: 232px;
    font-size: 19px; line-height: 23px; color: var(--white); font-weight: 400;
  }
  .doctor {
    position: absolute; left: 748px; top: 318px;
    font-size: 44px; line-height: 44px; font-weight: 700; color: var(--green-text);
  }
  .practice {
    position: absolute; right: 65px; top: 417px;
    font-size: 22px; line-height: 22px; font-weight: 700; color: var(--white);
  }
  .bands { position: absolute; left: 0; top: 450px; width: 1200px; height: 90px; }
  .insurance {
    position: absolute; left: 25px; top: 457px; color: var(--ink);
  }
  .insurance-list { font-size: 19px; line-height: 22px; font-weight: 700; }
  .walk-in {
    margin-top: 4px; font-size: 36px; line-height: 40px; font-weight: 700; color: var(--white);
  }
  .tagline {
    position: absolute; left: 495px; top: 468px;
    font-size: 48px; line-height: 52px; font-weight: 700; color: var(--white);
    white-space: nowrap;
  }
</style>
</head>
<body>
  <main class="banner">
    <div class="family-photo" role="img" aria-label="Photo of a smiling mother and daughter hugging, both wearing black-rimmed glasses"></div>

    <div class="phone">
      <svg class="phone-icon" viewBox="0 0 40 40" aria-hidden="true">
        <rect width="40" height="40" rx="7" fill="var(--yellow)"/>
        <path d="M13 9c1.5-.8 2.6-.4 3.3.9l2 3.8c.6 1.2.3 2.2-.8 3l-1.3 1c1 2.6 3 4.7 5.7 6l1-1.3c.8-1 1.9-1.2 3-.6l3.8 2c1.3.7 1.6 1.9.8 3.3l-1.2 2c-1 1.6-3 2.2-5 1.5C17.4 28.9 11.3 22.8 9.5 16c-.6-2.2.1-4 1.6-5z" fill="#ffffff"/>
      </svg>
      <span>555.762.4139</span>
    </div>

    <div class="brand">
      <div class="brand-square"></div>
      <div class="brand-name">TALVIN<br>OPTOMETRY</div>
    </div>

    <p class="services">EYE EXAM, CONTACT LENS, ORTHOK,<br>LASIK CONSULTATION, DIABETES<br>RETINAL EXAM</p>
    <h1 class="doctor">DR. NORA PEL</h1>
    <p class="practice">TALVIN OPTOMETRY</p>

    <svg class="bands" viewBox="0 0 1200 90" preserveAspectRatio="none" aria-hidden="true">
      <polygon points="0,0 485,0 445,80 0,80" fill="var(--green)"/>
      <polygon points="497,5 1200,5 1200,90 455,90" fill="var(--teal)"/>
    </svg>
    <div class="insurance">
      <p class="insurance-list">MEDICAL, VITALBASE, QRT, BRAVELINK,</p>
      <p class="walk-in">WALK IN WELCOME</p>
    </div>
    <p class="tagline">“ Eyecare for your family”</p>
  </main>
</body>
</html>
```